Tarn - Stationary Design/Layout

We are a well established clothing design and manufacturing company (Tarn Sourcing) based in London UK, with our own factory in Bangladesh, supplying to many fashion retailers and brands. Our factory has very high environmental and ethical standards with people at its heart. Our quality of garments are second to none.
Our new logo has been proudly developed by the Pixel Guild community last month, we are now in the second phase and need the layout designed for our letterheads, double sided business cards, compliment slip and clothing ticket. Feel as creative as you like, but make sure it looks great!!
***The Logo - the logo design and colour is set and should NOT be changed and stay on a dark grey backround. The logo artwork to use is attached.
***Details to use for the business card:
Dorian Pelham
Direct Line: 020 7946 0158
dorian@tarnsourcing-example.com
Tarn Sourching Ltd.
57 - 59 Hollin Row
Fernley, Ashcombe
NW9 4QT
Switchboard: 020 7946 0274
Fax: 020 7946 0274
www.tarnsourcing-example.co.uk
***Details to use for the letterhead and compliment slip:
Tarn Sourching Ltd.
57 - 59 Hollin Row
Fernley, Ashcombe
NW9 4QT
Fax: 020 7946 0274
www.tarnsourcing-example.co.uk
***Details for Swing Ticket:
Size: 12cm height by 5.5cm width
One side need to have just the logo without the 'Sourcing', on the other it needs to stay blank

```html
<!DOCTYPE html>
<html lang="en">
<head>
<meta charset="utf-8">
<title>Tarn Sourcing – Letterhead</title>
<link rel="stylesheet" href="https://fonts.googleapis.com/css2?family=Crimson+Pro:wght@400&display=swap">
<style>
  :root {
    --charcoal: #3a3a3a;
    --aqua: #a9dde1;
    --paper: #ffffff;
  }
  html, body {
    margin: 0;
    padding: 0;
    overflow: hidden;
    background: var(--paper);
  }
  .letterhead {
    position: relative;
    width: 849px;
    height: 1200px;
    overflow: hidden;
    background: var(--paper);
    font-family: "Crimson Pro", "Palatino Linotype", serif;
  }
  .letterhead__frame {
    position: absolute;
    inset: 0;
    width: 849px;
    height: 1200px;
  }
  .frame__band, .frame__edge { fill: var(--charcoal); }
  .frame__stripe { fill: var(--aqua); }
  .brand-name {
    position: absolute;
    left: 35px;
    top: 64px;
    margin: 0;
    font-size: 52px;
    font-weight: 400;
    letter-spacing: 2.5px;
    line-height: 1;
    color: var(--aqua);
    white-space: nowrap;
  }
  .company-details {
    position: absolute;
    right: 26px;
    top: 9px;
    margin: 0;
    text-align: right;
    font-style: normal;
    font-size: 18px;
    line-height: 19.3px;
    color: var(--aqua);
  }
  .company-details p { margin: 0; }
  .company-details .contact-lines { margin-top: 16px; }
</style>
</head>
<body>
  <main class="letterhead">
    <svg class="letterhead__frame" viewBox="0 0 849 1200" aria-hidden="true">
      <rect class="frame__band" x="0" y="0" width="849" height="177"/>
      <path class="frame__stripe" d="M0 176 L71 176 Q30 560 24 1200 L0 1200 Z"/>
      <path class="frame__edge" d="M0 176 L58 176 Q18 560 14 1200 L0 1200 Z"/>
    </svg>

    <h1 class="brand-name">Tarn Sourcing</h1>

    <address class="company-details">
      <p>Tarn Sourching Ltd</p>
      <p>57 - 59 Hollin Row</p>
      <p>Fernley, Ashcombe</p>
      <p>NW9 4QT</p>
      <div class="contact-lines">
        <p>Switchboard: 020 7946 0274</p>
        <p>Fax: 020 7946 0274</p>
        <p>www.tarnsourcing-example.co.uk</p>
      </div>
    </address>
  </main>
</body>
</html>
```